Stationary and Business Card Design

We need a stationery design and a business card design for a non-profit economics development agency. Our website is growharborline.org. Our clients are Canadian government agencies and large Chinese company. We need the design to be professional and corporate.

Please see attached for our Power Point presentation. Please take design elements from our website and our ppt.

```html
<!DOCTYPE html>
<html lang="en">
<head>
<meta charset="utf-8">
<title>Harborline Growth Alliance — Stationery</title>
<link rel="stylesheet" href="https://fonts.googleapis.com/css2?family=Open+Sans:wght@400;600;700&display=swap">
<style>
  :root {
    --brand-red: #e60012;
    --ink: #111111;
    --paper: #ffffff;
    --envelope-edge: #e9eaeb;
    --stage: #ffffff;
  }
  * { box-sizing: border-box; margin: 0; padding: 0; }
  html, body { width: 1200px; height: 947px; overflow: hidden; background: var(--stage); }
  body { position: relative; font-family: "Open Sans", Arial, sans-serif; color: var(--ink); }

  .sheet { position: absolute; background: var(--paper); box-shadow: 2px 3px 8px rgba(0,0,0,.35); overflow: hidden; }
  .band { position: absolute; left: 0; right: 0; bottom: 0; background: var(--brand-red); color: #fff;
          font-weight: 600; text-align: center; display: flex; align-items: center; justify-content: center; }

  .brand { position: absolute; display: flex; align-items: center; gap: 6px; color: var(--brand-red); font-weight: 700; white-space: nowrap; }
  .brand-mark { background: var(--brand-red); flex: none; }

  address { font-style: normal; }

  /* Letterhead */
  .letterhead { left: 84px; top: 29px; width: 620px; height: 879px; }
  .letterhead .brand { left: 54px; top: 60px; font-size: 17px; }
  .letterhead .brand-mark { width: 16px; height: 16px; }
  .letterhead .band { height: 27px; font-size: 9px; }
  .letterhead .address { position: absolute; right: 28px; top: 36px; text-align: right; font-size: 10px; font-weight: 600; line-height: 14px; }
  .letterhead .contacts { position: absolute; right: 28px; top: 116px; font-size: 10px; font-weight: 600; line-height: 13px; text-align: right; }

  .contact-line { display: flex; align-items: center; justify-content: flex-end; gap: 4px; }
  .contact-line svg { fill: var(--brand-red); flex: none; }

  /* Business card front */
  .card-front { left: 734px; top: 102px; width: 281px; height: 158px; }
  .card-front .brand { left: 20px; top: 18px; font-size: 11px; gap: 4px; }
  .card-front .brand-mark { width: 10px; height: 10px; }
  .card-front .person { position: absolute; left: 20px; top: 64px; }
  .card-front .person-name { color: var(--brand-red); font-size: 10.5px; font-weight: 700; line-height: 13px; }
  .card-front .person-role { font-size: 8px; font-weight: 600; }
  .card-front .address { position: absolute; left: 20px; top: 103px; font-size: 5.4px; font-weight: 700; line-height: 8px; }
  .card-front .contacts { position: absolute; left: 115px; top: 102px; font-size: 5.4px; font-weight: 700; line-height: 7.5px; }
  .card-front .contact-line { justify-content: flex-start; gap: 3px; }
  .card-front .band { height: 15px; font-size: 6.5px; }

  /* Business card back */
  .card-back { left: 734px; top: 282px; width: 281px; height: 160px; background: var(--brand-red); }
  .card-back .brand { left: 0; right: 0; top: 72px; justify-content: center; color: #fff; font-size: 13px; }

  /* Envelope */
  .envelope { left: 423px; top: 510px; width: 690px; height: 348px;
              background: radial-gradient(ellipse 60% 75% at 60% 45%, #ffffff 55%, var(--envelope-edge) 100%); }
  .envelope .brand { left: 30px; top: 40px; font-size: 17px; }
  .envelope .brand-mark { width: 16px; height: 16px; }
  .envelope .address { position: absolute; left: 30px; top: 118px; font-size: 10.5px; font-weight: 600; line-height: 14px; }
  .envelope .band { height: 28px; font-size: 9px; }
</style>
</head>
<body>

<section class="sheet letterhead" aria-label="Letterhead">
  <div class="brand"><span class="brand-mark"></span>Harborline Growth Alliance</div>
  <address class="address">
    2750 Lakeview Rd. East,<br>Suite 412<br>Oakridge, Ontario,<br>L4B 2K6
  </address>
  <div class="contacts">
    <div class="contact-line"><svg width="8" height="8" viewBox="0 0 10 10"><path d="M2 0h2l1 3-1.5 1a6 6 0 0 0 2.5 2.5L7 5l3 1v2a2 2 0 0 1-2 2A8 8 0 0 1 0 2a2 2 0 0 1 2-2z"/></svg>416 555 0174</div>
    <div class="contact-line"><svg width="8" height="8" viewBox="0 0 10 10"><path d="M2 0h6v3H2zM0 4h10v4H8v2H2V8H0zM3 6v3h4V6z"/></svg>416 555 0175</div>
    <div class="contact-line"><svg width="8" height="7" viewBox="0 0 10 8"><path d="M0 0h10v8H0zM1 1l4 3 4-3z" fill-rule="evenodd"/></svg>info@growharborline.org</div>
    <div class="contact-line"><svg width="8" height="8" viewBox="0 0 10 10"><circle cx="5" cy="5" r="4.2" fill="none" stroke="#e60012" stroke-width="1.2"/><path d="M1 5h8M5 1v8" stroke="#e60012" stroke-width=".9"/></svg>www.growharborline.org</div>
  </div>
  <div class="band">Your Trusted Growth Partner!</div>
</section>

<section class="sheet card-front" aria-label="Business card, front">
  <div class="brand"><span class="brand-mark"></span>Harborline Growth Alliance</div>
  <div class="person">
    <div class="person-name">Mark Ellison</div>
    <div class="person-role">Director</div>
  </div>
  <address class="address">
    2750 Lakeview Rd. East,<br>Suite 412<br>Oakridge, Ontario,<br>L4B 2K6
  </address>
  <div class="contacts">
    <div class="contact-line"><svg width="5" height="5" viewBox="0 0 10 10"><path d="M2 0h2l1 3-1.5 1a6 6 0 0 0 2.5 2.5L7 5l3 1v2a2 2 0 0 1-2 2A8 8 0 0 1 0 2a2 2 0 0 1 2-2z"/></svg>416 555 0174</div>
    <div class="contact-line"><svg width="5" height="5" viewBox="0 0 10 10"><path d="M2 0h6v3H2zM0 4h10v4H8v2H2V8H0zM3 6v3h4V6z"/></svg>416 555 0175</div>
    <div class="contact-line"><svg width="5" height="4" viewBox="0 0 10 8"><path d="M0 0h10v8H0zM1 1l4 3 4-3z" fill-rule="evenodd"/></svg>info@growharborline.org</div>
    <div class="contact-line"><svg width="5" height="5" viewBox="0 0 10 10"><circle cx="5" cy="5" r="4.2" fill="none" stroke="#e60012" stroke-width="1.4"/></svg>www.growharborline.org</div>
  </div>
  <div class="band">Your Trusted Growth Partner!</div>
</section>

<section class="sheet card-back" aria-label="Business card, back">
  <div class="brand">Harborline Growth Alliance</div>
</section>

<section class="sheet envelope" aria-label="Envelope">
  <div class="brand"><span class="brand-mark"></span>Harborline Growth Alliance</div>
  <address class="address">
    2750 Lakeview Rd. East,<br>Suite 412<br>Oakridge, Ontario,<br>L4B 2K6
  </address>
  <div class="band">Your Trusted Growth Partner!</div>
</section>

</body>
</html>
```